Menu Re-Design for The Marlowbrook a british eatery in spanish holiday resort

Looking for a new design for our breakfast and lunch menu....

I have included some pictures of a few menus I like the feel of File No 1,2,3,4,5..... but am open to any ideas you may have....

The menu is to be double sided consisting of a front design with actual menu on reverse....

I have also included the relevant text files you will require...

We do not have a logo or set colour scheme to follow...

Target Market(s)

Predominantly British holidaymakers in popular Spanish resort....

Requirements
Must have
• Menu to be A3 and double sided, split between either a front page design and menu on reverse, or menu divided between both sides....
• Company Name:- The Marlowbrook
Nice to have
• Fun and Bold design whilst maintaining a feel of quality....
Should not have
• Please avoid the use of any food photography....

```html
<!DOCTYPE html>
<html lang="en">
<head>
<meta charset="utf-8">
<title>The Marlowbrook – Breakfast &amp; Lunch Menu</title>
<link href="https://fonts.googleapis.com/css2?family=Libre+Baskerville:wght@700&family=Open+Sans:ital,wght@0,400;0,600;0,700;0,800;1,400;1,700;1,800&display=swap" rel="stylesheet">
<style>
:root{
  --bg:#8c8c8c;
  --paper:#fcefd6;
  --red:#b2283e;
  --brown:#6a4733;
  --ink:#231f20;
  --text:#3a302a;
  --sketch:#d9c3a4;
}
*{box-sizing:border-box;margin:0;padding:0}
html,body{width:1200px;height:1200px;overflow:hidden}
body{background:var(--bg);font-family:"Open Sans",Arial,sans-serif;color:var(--text)}
.sheet{position:absolute;left:200px;width:900px;height:637px;background:var(--paper);transform-origin:0 0;transform:scale(.889);box-shadow:0 2px 10px rgba(0,0,0,.35);overflow:hidden}
.sheet--front{top:24px}
.sheet--back{top:610px}
.sheet::after{content:"";position:absolute;left:450px;top:0;bottom:0;width:1px;background:rgba(0,0,0,.05)}
.abs{position:absolute}
.wordmark{font-family:"Libre Baskerville",Georgia,serif;font-weight:700;color:var(--brown);white-space:nowrap}
.masthead{left:22px;top:42px;font-size:35px;line-height:1}
.tagline{left:22px;top:98px;width:340px;display:flex;align-items:center;gap:8px;font-family:"Libre Baskerville",Georgia,serif;font-weight:700;font-size:15px;color:var(--ink)}
.tagline::before,.tagline::after{content:"";flex:1;height:1.5px;background:var(--ink)}
.mini-mark{font-size:17px;text-align:right}
.mini-mark small{display:block;font-size:5.5px;color:var(--ink);letter-spacing:.5px;margin-top:1px}
.art{background:linear-gradient(135deg,rgba(217,195,164,.55),rgba(217,195,164,.15))}
.band{background:var(--red);height:28px;display:flex;align-items:center;padding:0 10px;color:#fff}
.band h2{font-style:italic;font-weight:800;font-size:23px;line-height:1}
.band .note{font-style:italic;font-weight:700;font-size:8px;line-height:1;margin-left:10px}
.band .icons{margin-left:auto;display:flex;gap:4px}
.head{font-style:italic;font-weight:800;color:var(--ink);line-height:1}
.item-name{color:var(--red);font-weight:700;font-size:13px}
.desc{font-size:10.5px;line-height:16px;color:var(--ink)}
.red-note{font-style:italic;color:var(--red);font-size:7px}
.list{list-style:none;font-size:9.3px;color:var(--ink)}
.list li{display:flex;justify-content:space-between;height:17.8px;align-items:center}
.list--tight li{height:13px}
.rule{position:absolute;background:var(--ink)}
.special{position:absolute;left:483px;width:387px}
.special .row{display:flex;justify-content:space-between}
.special .row b{color:var(--red);font-size:11.5px}
.special p{font-size:8.8px;line-height:13px;color:var(--ink);margin-top:1px}
.para{font-size:8px;line-height:12px;color:var(--red)}
.para em{font-style:italic}
.ref{font-size:5px;color:var(--red)}
.chef{background:var(--ink);color:#fff}
.burger-item{display:flex;justify-content:space-between;color:var(--red);font-weight:700;font-size:11.5px;height:22px}
.salad-row{display:flex;justify-content:space-between;align-items:flex-end;height:29px}
</style>
</head>
<body>

<section class="sheet sheet--front" aria-label="Breakfast menu">
  <div class="abs art" style="left:372px;top:14px;width:236px;height:170px" role="img" aria-label="Sketch of a cooking pot, frying pan and bread"></div>
  <div class="abs wordmark masthead">The Marlowbrook</div>
  <div class="abs tagline">BREAKFAST &amp; LUNCH</div>

  <p class="abs para" style="left:615px;top:22px;width:263px;text-align:right;font-size:7.8px;line-height:11.8px">a <em>FULL BREAKFAST</em> is a breakfast meal, usually including bacon, sausages, eggs, a variety of other cooked foods and a beverage such as coffee or tea that originated in England or Ireland. It is especially popular in the UK and Ireland, to the extent that many cafés and pubs offer the meal at any time of day as an "all-day breakfast". In England it is usually referred to as a 'full English breakfast' (often shortened to 'full English') or 'fry-up'. <span class="ref">foodlore.org/full-breakfast</span></p>

  <div class="abs band" style="left:22px;top:137px;width:321px">
    <h2>Breakfast</h2>
    <span class="icons"><svg width="88" height="18" viewBox="0 0 88 18" fill="#fff"><path d="M2 15h18v2H2zM4 14a7 7 0 0 1 14 0z"/><circle cx="32" cy="9" r="8"/><path d="M46 8h12v3a6 6 0 0 1-12 0zM58 9h3v2h-3z"/><path d="M70 9a8 6 0 0 1 16 0zM70 11h16v2H70zM70 14h16a2 2 0 0 1-2 3H72a2 2 0 0 1-2-3z"/></svg></span>
  </div>

  <svg class="abs" style="left:304px;top:150px" width="80" height="80" viewBox="0 0 80 80" aria-label="Served until 5PM">
    <polygon fill="#1d1a1b" points="40,0 46,12 58,4 59,18 74,14 68,28 80,34 68,42 76,55 62,56 62,71 49,65 42,80 35,67 22,75 20,61 6,62 12,49 0,40 12,32 5,19 19,19 20,5 33,12"/>
    <g fill="#fff" font-family="Open Sans,Arial,sans-serif" font-weight="800" font-style="italic" text-anchor="middle" transform="rotate(-12 40 40)">
      <text x="40" y="32" font-size="10">SERVED</text>
      <text x="40" y="40" font-size="5">UNTIL</text>
      <text x="40" y="55" font-size="17">5PM</text>
    </g>
  </svg>

  <div class="abs" style="left:30px;top:178px;width:270px">
    <div style="display:flex;justify-content:space-between"><span class="item-name">MARLOWBROOK</span><span class="item-name">4.50</span></div>
    <p class="desc">Bacon, Fried Egg, Sausage,<br>Beans or Grilled Tomato, Toast &amp; Butter</p>
  </div>
  <div class="abs" style="left:30px;top:247px;width:270px">
    <div style="display:flex;justify-content:space-between"><span class="item-name">HEARTY</span><span class="item-name">6.50</span></div>
    <p class="desc">2 Bacon, 2 Fried eggs, 2 Sausage,<br>Beans or Grilled Tomato, Toast &amp; Butter</p>
  </div>
  <p class="abs red-note" style="left:32px;top:307px;font-weight:700">Any changes made to set breakfast, will be charged as Build Your Own.</p>

  <div class="abs" style="left:310px;top:236px;width:112px">
    <div style="display:flex;align-items:flex-end;gap:4px">
      <span class="head" style="color:var(--red);font-size:24px;transform:rotate(-6deg)">FREE!</span>
      <svg width="36" height="36" viewBox="0 0 36 36" fill="var(--red)"><path d="M4 16h22v6a11 11 0 0 1-22 0z"/><path d="M26 18h4a4 4 0 0 1 0 8h-5v-2h5a2 2 0 0 0 0-4h-4z"/><path d="M2 33h28v2H2z"/><path d="M16 2c3 3-3 5 0 9" stroke="var(--red)" stroke-width="2" fill="none"/></svg>
    </div>
    <p class="head" style="font-size:11.5px;text-align:right;line-height:15px;margin-top:2px">Tea, Coffe <span style="font-size:8px">or</span><br>Orange Juice</p>
  </div>

  <div class="rule" style="left:22px;top:330px;width:400px;height:1px"></div>

  <div class="abs chef" style="left:22px;top:345px;width:117px;height:256px">
    <div class="art" style="height:103px;background:linear-gradient(180deg,#b2283e 0%,#7a1d2c 100%)" role="img" aria-label="Illustration of a moustached chef in a tall hat"></div>
    <p class="head" style="color:#fff;font-size:13px;margin:12px 0 0 22px">Chef said...</p>
    <p style="font-size:8.6px;line-height:13px;text-align:center;padding:8px 8px 0 12px;position:relative">
      <span style="position:absolute;left:6px;top:-2px;font:800 30px/1 Georgia,serif">“</span>
      &nbsp;&nbsp;&nbsp;All our Breakfast ingredients are of the highest quality available, sourced directly from the UK and freshly cooked to order
      <span style="position:absolute;right:4px;bottom:-22px;font:800 30px/1 Georgia,serif">”</span>
    </p>
  </div>

  <h3 class="abs head" style="left:151px;top:343px;font-size:23px">Build Your Own</h3>
  <p class="abs" style="left:367px;top:347px;color:var(--red);font-weight:700;font-size:7px;line-height:9px">Min. order of<br><span style="font-size:10px">3.50</span> euros</p>
  <ul class="abs list" style="left:151px;top:376px;width:262px">
    <li><span>Sausage</span><span>1.00</span></li>
    <li><span>Fried Egg</span><span>75c</span></li>
    <li><span>Bacon</span><span>1.00</span></li>
    <li><span>Beans</span><span>50c</span></li>
    <li><span>Black Pudding</span><span>1.00</span></li>
    <li><span>Grilled Tomato</span><span>50c</span></li>
    <li><span>Fried Bread</span><span>1.00</span></li>
    <li><span>Hash Brown</span><span>75c</span></li>
    <li><span>Mushrooms</span><span>1.25</span></li>
    <li><span>2 Bread &amp; Butter</span><span>1.00</span></li>
    <li><span>Poached Egg</span><span>1.50</span></li>
    <li><span>2 Toast &amp; Butter</span><span>1.50</span></li>
    <li><span>Scrambled Eggs</span><span>2.00</span></li>
  </ul>

  <h3 class="abs head" style="left:597px;top:133px;font-size:24px;line-height:1.1">&nbsp;&nbsp;&nbsp;&nbsp;&nbsp;&nbsp;Breakfast<br>Snacks</h3>
  <ul class="abs list" style="left:483px;top:182px;width:162px">
    <li><span>2 fried eggs on toast</span><span>3.50</span></li>
    <li><span>Scrambled eggs on toast</span><span>3.50</span></li>
    <li><span>Poached eggs on toast</span><span>4.00</span></li>
    <li><span>Beans on toast</span><span>3.50</span></li>
    <li><span>Toast and preserves</span><span>2.50</span></li>
  </ul>
  <ul class="abs list" style="left:690px;top:164px;width:176px">
    <li><span>Sausage sandwich</span><span>4.00</span></li>
    <li><span>Bacon sandwich</span><span>4.00</span></li>
    <li><span>Fried Egg sandwich</span><span>3.50</span></li>
    <li><span>Bacon &amp; Egg sandwich</span><span>4.50</span></li>
    <li><span>Sausage &amp; Egg sandwich</span><span>4.50</span></li>
    <li><span>Sausage &amp; Bacon sandwich</span><span>5.00</span></li>
  </ul>

  <div class="abs band" style="left:476px;top:280px;width:400px">
    <h2>Something Different?</h2>
    <span class="icons"><svg width="88" height="18" viewBox="0 0 88 18" fill="#fff"><path d="M2 15h18v2H2zM4 14a7 7 0 0 1 14 0z"/><circle cx="32" cy="9" r="8"/><path d="M46 8h12v3a6 6 0 0 1-12 0zM58 9h3v2h-3z"/><path d="M70 9a8 6 0 0 1 16 0zM70 11h16v2H70zM70 14h16a2 2 0 0 1-2 3H72a2 2 0 0 1-2-3z"/></svg></span>
  </div>

  <div class="special" style="top:317px"><div class="row"><b>EGGS BENEDICT</b><b>5.50</b></div><p>Traditional eggs benedict with home baked ham and soft poached eggs<br>coated in a rich hollandaise sauce on a toasted english muffin</p></div>
  <div class="special" style="top:373px"><div class="row"><b>EGGS ROYALE</b><b>6.00</b></div><p>smoked salmon on a toasted english muffin softly poached eggs<br>and a covering of hollandaise sauce</p></div>
  <div class="special" style="top:428px"><div class="row"><b>PANCAKE STACK</b><b>6.50</b></div><p>american style pancakes with crispy bacon and maple syrup</p></div>
  <div class="special" style="top:470px"><div class="row"><b>SMOKED AND SCRAMBLED</b><b>6.50</b></div><p>smoked salmon with creamy scrambled eggs served with wholemeal toast</p></div>
  <div class="special" style="top:513px"><div class="row"><b>BIG BREAKFAST WRAP</b><b>5.50</b></div><p>sausage bacon 2 egg omelette and hash brown served in a soft flour tortilla wrap</p></div>
  <div class="special" style="top:555px"><div class="row"><b>BREAKFAST MUFFIN</b><b>5.00</b></div><p>bacon or sausage on a toasted english muffin with<br>mature cheddar cheese and a perfectly fried egg</p></div>

  <div class="abs wordmark mini-mark" style="right:22px;top:586px">The Marlowbrook<small>BREAKFAST &amp; LUNCH</small></div>
  <div class="rule" style="left:22px;top:612px;width:856px;height:1px"></div>
</section>

<section class="sheet sheet--back" aria-label="Lunch menu">
  <div class="abs band" style="left:20px;top:27px;width:400px">
    <h2>Burgers</h2><span class="note">All served with a salad garnish<br>and homemade coleslaw</span>
    <span class="icons"><svg width="88" height="18" viewBox="0 0 88 18" fill="#fff"><path d="M2 15h18v2H2zM4 14a7 7 0 0 1 14 0z"/><circle cx="32" cy="9" r="8"/><path d="M46 8h12v3a6 6 0 0 1-12 0zM58 9h3v2h-3z"/><path d="M70 9a8 6 0 0 1 16 0zM70 11h16v2H70zM70 14h16a2 2 0 0 1-2 3H72a2 2 0 0 1-2-3z"/></svg></span>
  </div>
  <div class="abs" style="left:24px;top:63px;width:386px">
    <div class="burger-item"><span>1/2 LB HOMEMADE ABERDEEN ANGUS</span><span>6.50</span></div>
    <div class="burger-item"><span>1/4 LB 100% IRISH BEEF</span><span>4.50</span></div>
    <div class="burger-item"><span>100% CHICKEN BREAST (BATTERED)</span><span>5.00</span></div>
  </div>
  <p class="abs" style="left:24px;top:127px;font-size:9.3px;color:var(--ink)">Add any extra of your choice :</p>
  <ul class="abs list" style="left:24px;top:141px;width:194px">
    <li style="height:14.5px"><span>- &nbsp; Onion</span><span>50c</span></li>
    <li style="height:14.5px"><span>- &nbsp; Cheddar Cheese</span><span>1.00</span></li>
    <li style="height:14.5px"><span>- &nbsp; Onion Rings</span><span>1.00</span></li>
    <li style="height:14.5px"><span>- &nbsp; Bacon</span><span>1.00</span></li>
    <li style="height:14.5px"><span>- &nbsp; Chilli Con Carne</span><span>1.50</span></li>
    <li style="height:14.5px"><span>- &nbsp; Homemade Chips</span><span>2.00</span></li>
    <li style="height:14.5px"><span>- &nbsp; Spicy Potato Wedges</span><span>2.00</span></li>
  </ul>

  <div class="rule" style="left:235px;top:135px;width:1px;height:478px"></div>
  <div class="rule" style="left:235px;top:135px;width:185px;height:1px"></div>
  <div class="rule" style="left:20px;top:258px;width:215px;height:1px"></div>
  <div class="rule" style="left:235px;top:347px;width:185px;height:1px"></div>

  <h3 class="abs head" style="left:248px;top:142px;font-size:13.5px">Fresh Baked</h3>
  <h3 class="abs head" style="left:248px;top:158px;font-size:24px">Baguettes</h3>
  <p class="abs" style="left:248px;top:187px;font-size:7px;line-height:8px;color:var(--ink)">served with homemadehand-cut chips,<br>salad and coleslaw</p>
  <div class="abs" style="left:248px;top:210px;width:168px;font-size:9.3px;color:var(--ink)">
    <div style="display:flex;justify-content:space-between;height:17px"><span>Tuna Cheese Melt</span><span>7.50</span></div>
    <div style="display:flex;justify-content:space-between"><span>Hunters Chicken</span><span>7.50</span></div>
    <div style="font-size:6.8px;font-style:italic;height:12px">(chicken, bacon, bbq sauce, melted cheese)</div>
    <div style="display:flex;justify-content:space-between;height:18px;align-items:center"><span>B L T</span><span>7.50</span></div>
    <div style="display:flex;justify-content:space-between;height:17px"><span>Chicken Tikka in Minted Mayo</span><span>7.50</span></div>
    <div style="display:flex;justify-content:space-between;align-items:flex-end;line-height:13px;height:31px"><span>Pork &amp; Herb Sausage<br>with Fried Onion</span><span>7.50</span></div>
    <div style="display:flex;justify-content:space-between;height:17px;align-items:center"><span>Chicken &amp; Bacon Mayo</span><span>7.50</span></div>
  </div>

  <h3 class="abs head" style="left:24px;top:267px;font-size:15px">Jacket</h3>
  <h3 class="abs head" style="left:24px;top:283px;font-size:21px">Potatoes</h3>
  <p class="abs" style="left:80px;top:271px;font-style:italic;font-size:7.5px;color:var(--ink)">served with salad garnish and</p>
  <p class="abs" style="left:132px;top:291px;font-style:italic;font-size:7.5px;color:var(--ink)">homemade coleslaw</p>
  <ul class="abs list" style="left:26px;top:310px;width:190px">
    <li><span>Plain</span><span>4.50</span></li>
    <li><span>Baked Beans</span><span>5.50</span></li>
    <li><span>Cheddar Cheese</span><span>5.50</span></li>
    <li><span>Tuna Mayonnaise</span><span>5.50</span></li>
    <li><span>Curry Sauce</span><span>5.50</span></li>
    <li><span>Beans &amp; Cheese</span><span>6.00</span></li>
    <li><span>Chicken Curry</span><span>6.50</span></li>
    <li><span>Chilli</span><span>6.50</span></li>
  </ul>
  <p class="abs" style="left:25px;top:459px;width:198px;font-size:7.8px;line-height:12px;color:var(--text)">»» a <em>JACKET POTATO</em> is another name of baked potato called in the United Kingdom. The baked potato has been popular in the UK for many years. In the mid-19th century, jacket potatoes were sold on the streets by hawkers during the autumn and winter months. In London, it was estimated that some 10 tons of baked potatoes were sold each day by this method. Common jacket potato fillings (or "toppings") in the United Kingdom include cheese and beans, tuna mayonnaise, chili con carne and chicken and bacon. <span style="font-size:5px">foodlore.org/baked-potato</span></p>

  <h3 class="abs head" style="left:250px;top:360px;font-size:23px">Omelettes</h3>
  <p class="abs" style="left:252px;top:384px;font-style:italic;font-size:7px;line-height:8px;color:var(--ink)">served with salad garnish<br>and homemade coleslaw</p>
  <ul class="abs list" style="left:248px;top:403px;width:166px">
    <li><span>Plain</span><span>5.00</span></li>
    <li><span>Cheddar Cheese</span><span>5.50</span></li>
    <li><span>Ham</span><span>5.50</span></li>
    <li><span>Mushroom</span><span>5.50</span></li>
    <li><span>Cheese &amp; Onion</span><span>6.00</span></li>
    <li><span>Cheese &amp; Ham</span><span>6.00</span></li>
    <li><span>Bacon</span><span>6.00</span></li>
    <li><span>Bacon &amp; Cheese</span><span>6.50</span></li>
  </ul>
  <p class="abs red-note" style="left:248px;top:557px">Add homemade chips 2.00</p>

  <div class="abs band" style="left:480px;top:27px;width:396px">
    <h2>Sandwiches</h2><span class="note">Served with a salad garnish<br>and homemade coleslaw</span>
    <span class="icons"><svg width="88" height="18" viewBox="0 0 88 18" fill="#fff"><path d="M2 15h18v2H2zM4 14a7 7 0 0 1 14 0z"/><circle cx="32" cy="9" r="8"/><path d="M46 8h12v3a6 6 0 0 1-12 0zM58 9h3v2h-3z"/><path d="M70 9a8 6 0 0 1 16 0zM70 11h16v2H70zM70 14h16a2 2 0 0 1-2 3H72a2 2 0 0 1-2-3z"/></svg></span>
  </div>
  <ul class="abs list" style="left:484px;top:59px;width:240px">
    <li><span>Mature Cheddar Cheese</span><span>4.00</span></li>
    <li><span>Bacon &amp; Cheese</span><span>5.00</span></li>
    <li><span>Home Baked Ham</span><span>4.50</span></li>
    <li><span>BLT</span><span>5.00</span></li>
    <li><span>Tuna Mayonnaise</span><span>4.50</span></li>
    <li><span>Cheese &amp; Home Baked Ham</span><span>5.00</span></li>
    <li><span>Chicken Mayonnaise</span><span>4.50</span></li>
    <li><span>Chicken &amp; Bacon Mayonnaise</span><span>5.50</span></li>
  </ul>
  <p class="abs red-note" style="left:484px;top:213px">Any of the above are also available as a floury soft roll or toastie</p>
  <div class="rule" style="left:480px;top:233px;width:250px;height:1px"></div>

  <p class="abs head" style="left:745px;top:60px;color:var(--red);font-family:'Courier New',monospace;font-size:20px;transform:rotate(-8deg)">Fact!</p>
  <p class="abs para" style="left:748px;top:80px;width:120px;text-align:right">a <em>SANDWICH</em> is a food item commonly consisting of two or more slices of bread, with one or more fillings between them. Sandwiches are a widely popular type of lunch food, typically taken to work, school, or picnics to be eaten as part of a packed lunch.</p>
  <p class="abs ref" style="right:32px;top:205px">foodlore.org/sandwich</p>
  <div class="abs art" style="left:780px;top:216px;width:118px;height:90px" role="img" aria-label="Sketch of a stacked sandwich"></div>

  <h3 class="abs head" style="left:484px;top:240px;font-size:24px">Wraps</h3>
  <p class="abs" style="left:486px;top:268px;font-style:italic;font-size:7.5px;line-height:8.5px;color:var(--ink)">Chicken Breast sautéd with red pepper and onion<br>with crisp lettuce in a Tortilla Wrap</p>
  <ul class="abs list" style="left:487px;top:291px;width:129px">
    <li><span>BBQ</span><span>6.50</span></li>
    <li><span>Cajun</span><span>6.50</span></li>
    <li><span>Tikka</span><span>6.50</span></li>
    <li><span>Sweet Chilli</span><span>6.50</span></li>
    <li><span>Garlic</span><span>6.50</span></li>
  </ul>
  <p class="abs red-note" style="left:487px;top:384px;width:129px;display:flex;justify-content:space-between"><span>Add Homemade Chips</span><span>2.00</span></p>
  <div class="rule" style="left:640px;top:290px;width:1px;height:110px"></div>

  <h3 class="abs head" style="left:662px;top:290px;font-size:24px">Salads</h3>
  <div class="abs" style="left:661px;top:313px;width:215px;font-size:9.3px;line-height:12.5px;color:var(--ink)">
    <div class="salad-row"><span>Creamy Goats Cheese<br>with Pedro Ximenez Glaze</span><span>7.00</span></div>
    <div class="salad-row"><span>Classic Chicken Caesar<br>&amp; Parmesan Shavings</span><span>7.00</span></div>
    <div class="salad-row"><span>Marlowbrook Mixed Salad<br>with House Dressing</span><span>6.50</span></div>
  </div>
  <div class="rule" style="left:480px;top:408px;width:398px;height:1px"></div>

  <h3 class="abs head" style="left:506px;top:417px;font-size:20px;line-height:21px;text-align:right;width:112px">Little Bites<br><span style="font-size:14px">&amp;</span> Sides</h3>
  <div class="abs art" style="left:508px;top:462px;width:110px;height:128px" role="img" aria-label="Sketch of a carton of chips"></div>
  <ul class="abs list list--tight" style="left:631px;top:419px;width:237px">
    <li><span>Basket of Homemade Chips</span><span>3.50</span></li>
    <li><span>Basket of Spicy Wedges</span><span>3.50</span></li>
    <li><span>Basket of Onion Rings</span><span>3.50</span></li>
    <li><span>Potato Skins with Cheese &amp; Bacon</span><span>4.50</span></li>
    <li><span>Cheesy Chilli Chips</span><span>6.00</span></li>
    <li><span>Cheesy Chilli Nachos</span><span>6.50</span></li>
    <li><span>Cheesy Chips</span><span>4.50</span></li>
    <li><span>Chilli &amp; Chips</span><span>5.00</span></li>
    <li><span>Curry Sauce &amp; Chips</span><span>4.50</span></li>
    <li><span>Garlic Bread</span><span>3.50</span></li>
    <li><span>Toasted Tea-Cake with Jam</span><span>3.00</span></li>
    <li><span>Fruit Scone with Cream &amp; Jam</span><span>3.00</span></li>
  </ul>

  <div class="abs wordmark mini-mark" style="right:22px;top:586px">The Marlowbrook<small>BREAKFAST &amp; LUNCH</small></div>
  <div class="rule" style="left:20px;top:612px;width:858px;height:1px"></div>
</section>

</body>
</html>
```